Business card design Needed for new logo / Construction business, home extensions and new builds

We need a business card design using our new logo files which i will attach to this project :)

We are a small construction business specialising in home extensions, new builds and property development. We are very ambitious and would appreciate professional and elegant designs for our new business card.

Very serious about using the services on Sketchwharf and recently acquired our new logo from here :)

Please get involved, i will feedback when i can as i am very busy but can respond daily, thanks

Target Market(s)

People that want to build onto their houses, new building developments or adding too their existing property

Industry/Entity Type

Construction

Contact Information for Business Card

Thornley Pike Construction, Wilbur Fenwick (Managing Director), Tel 07829456172, email - info@thornley-pike, www.thornley-pike.co.uk

Colors

Designer to choose colors to be used in the design.

Requirements
Must have
• I like a deep grey on the back please. A lot of you have provided black from and back, try mixing things up a little. The black looks cool 😎 Thanks

```html
<!DOCTYPE html>
<html lang="en">
<head>
<meta charset="utf-8">
<title>Thornley Pike Construction – Business Card</title>
<link rel="stylesheet" href="https://fonts.googleapis.com/css2?family=Cinzel:wght@600&family=Tinos&display=swap">
<style>
  :root {
    --backdrop: #232323;
    --card-grey: #666666;
    --gold: #d9a233;
    --silver: #dcdcdc;
    --ink-light: #ffffff;
  }
  * { box-sizing: border-box; margin: 0; padding: 0; }
  html, body {
    width: 1200px;
    height: 900px;
    overflow: hidden;
    background: var(--backdrop);
  }
  .canvas {
    position: relative;
    width: 1200px;
    height: 900px;
  }
  .card {
    position: absolute;
    left: 280px;
    width: 640px;
    height: 372px;
    background: var(--card-grey);
  }
  .card--front { top: 56px; }
  .card--back { top: 464px; }

  /* Front */
  .front-brand {
    position: absolute;
    inset: 0;
    display: flex;
    align-items: center;
    justify-content: center;
    gap: 14px;
  }
  .brand-mark {
    width: 18px;
    height: 18px;
    background: var(--gold);
  }
  .brand-name {
    font-family: "Cinzel", serif;
    font-weight: 600;
    font-size: 26px;
    letter-spacing: 1px;
    color: var(--silver);
  }

  /* Back */
  .back-brand {
    position: absolute;
    left: 44px;
    top: 44px;
  }
  .back-brand .brand-name { font-size: 24px; }
  .person {
    position: absolute;
    left: 44px;
    top: 138px;
  }
  .person-name {
    font-family: "Cinzel", serif;
    font-weight: 600;
    font-size: 24px;
    color: var(--gold);
    letter-spacing: 0.5px;
  }
  .person-role {
    font-family: "Tinos", serif;
    font-size: 18px;
    color: var(--ink-light);
    margin-top: 2px;
  }
  .contacts {
    position: absolute;
    left: 44px;
    top: 240px;
    list-style: none;
  }
  .contact {
    display: flex;
    align-items: center;
    gap: 10px;
    font-family: "Tinos", serif;
    font-size: 19px;
    color: var(--ink-light);
    margin-bottom: 10px;
  }
  .contact svg { width: 14px; height: 14px; flex: none; }
</style>
</head>
<body>
<main class="canvas">
  <section class="card card--front" aria-label="Card front">
    <div class="front-brand">
      <span class="brand-mark"></span>
      <span class="brand-name">Thornley Pike Construction</span>
    </div>
  </section>

  <section class="card card--back" aria-label="Card back">
    <div class="back-brand">
      <span class="brand-name">Thornley Pike Construction</span>
    </div>
    <div class="person">
      <p class="person-name">Wilbur Fenwick</p>
      <p class="person-role">Managing Director</p>
    </div>
    <ul class="contacts">
      <li class="contact">
        <svg viewBox="0 0 16 16" aria-hidden="true"><path fill="var(--gold)" d="M3 1l3 3-1.5 2a9 9 0 0 0 5.5 5.5L12 10l3 3-2 2C7 15 1 9 1 3z"/></svg>
        07829456172
      </li>
      <li class="contact">
        <svg viewBox="0 0 16 16" aria-hidden="true"><rect x="1" y="3" width="14" height="10" fill="var(--gold)"/><path d="M1 3l7 6 7-6" fill="none" stroke="var(--card-grey)" stroke-width="1.4"/></svg>
        info@thornley-pike
      </li>
      <li class="contact">
        <svg viewBox="0 0 16 16" aria-hidden="true"><circle cx="8" cy="8" r="6.5" fill="none" stroke="var(--gold)" stroke-width="1.6"/><path d="M1.5 8h13M8 1.5c-3 3.5-3 9.5 0 13M8 1.5c3 3.5 3 9.5 0 13" fill="none" stroke="var(--gold)" stroke-width="1.2"/></svg>
        www.thornley-pike.co.uk
      </li>
    </ul>
  </section>
</main>
</body>
</html>
```